Hydraulics Company Business Card Design

Modern business card design for a hydraulics company.
Our company colours are - black, orange and white.
I would like the following contact details included-
Name
Position
Phone number
Email
Website
Street Address

I have attached our company logo.
I would like the back of the card white.

Thank you.

```html
<!DOCTYPE html>
<html lang="en">
<head>
<meta charset="utf-8">
<title>Northgate Hydraulics – Business Card</title>
<link href="https://fonts.googleapis.com/css2?family=Poppins:wght@400;600;700&display=swap" rel="stylesheet">
<style>
  :root {
    --page-bg: #e9e7e3;
    --card-black: #111111;
    --card-black-edge: #050505;
    --emboss: #2c2c2c;
    --card-white: #ffffff;
    --orange: #f29a1f;
    --ink: #2a2a2a;
    --rule: #8a8a8a;
  }
  * { box-sizing: border-box; margin: 0; padding: 0; }
  html, body { width: 1200px; height: 900px; overflow: hidden; }
  body {
    background: var(--page-bg);
    font-family: "Poppins", sans-serif;
    position: relative;
  }
  .card {
    position: absolute;
    left: 260px;
    width: 680px;
    height: 389px;
    border-radius: 44px;
    box-shadow: 0 10px 28px rgba(0,0,0,0.18);
    overflow: hidden;
  }

  /* Front: black with tone-on-tone company name */
  .card--front {
    top: 40px;
    background: radial-gradient(ellipse at 50% 45%, #262626 0%, var(--card-black) 55%, var(--card-black-edge) 100%);
    display: flex;
    align-items: center;
    justify-content: center;
  }
  .front-name {
    font-weight: 700;
    font-size: 54px;
    letter-spacing: 1px;
    color: var(--emboss);
    line-height: 1;
  }

  /* Back: white with contact details */
  .card--back {
    top: 471px;
    background: linear-gradient(135deg, #f1f1f1 0%, var(--card-white) 60%, #f6f6f6 100%);
  }
  .back-name {
    position: absolute;
    top: 42px;
    right: 44px;
    font-weight: 700;
    font-size: 40px;
    color: var(--orange);
    line-height: 1;
  }
  .person {
    position: absolute;
    top: 196px;
    left: 42px;
    right: 56px;
  }
  .person__name {
    font-weight: 700;
    font-size: 20px;
    color: var(--orange);
    text-transform: uppercase;
    line-height: 1.1;
  }
  .person__role-row {
    display: flex;
    align-items: center;
    gap: 8px;
  }
  .person__role {
    font-size: 15px;
    color: var(--ink);
  }
  .person__rule {
    flex: 1;
    height: 1px;
    background: var(--rule);
  }
  .contacts {
    position: absolute;
    top: 266px;
    left: 60px;
    display: flex;
    align-items: flex-end;
    gap: 20px;
  }
  .contact-list { list-style: none; }
  .contact-list li {
    display: flex;
    align-items: center;
    gap: 10px;
    font-size: 15px;
    color: var(--ink);
    line-height: 1.75;
  }
  .contact-list svg { width: 17px; height: 17px; flex: none; }
  .address {
    border-left: 1px solid var(--ink);
    padding-left: 16px;
    font-size: 15px;
    color: var(--ink);
    line-height: 1.6;
    margin-bottom: 30px;
  }
</style>
</head>
<body>
  <section class="card card--front" aria-label="Card front">
    <p class="front-name">Northgate Hydraulics</p>
  </section>

  <section class="card card--back" aria-label="Card back">
    <p class="back-name">Northgate Hydraulics</p>

    <div class="person">
      <p class="person__name">Daniel Moreau</p>
      <div class="person__role-row">
        <span class="person__role">Owner</span>
        <span class="person__rule"></span>
      </div>
    </div>

    <div class="contacts">
      <ul class="contact-list">
        <li>
          <svg viewBox="0 0 24 24" aria-hidden="true"><path fill="var(--orange)" d="M6.6 10.8a15.1 15.1 0 0 0 6.6 6.6l2.2-2.2a1 1 0 0 1 1-.25 11.4 11.4 0 0 0 3.6.57 1 1 0 0 1 1 1V20a1 1 0 0 1-1 1A17 17 0 0 1 3 4a1 1 0 0 1 1-1h3.5a1 1 0 0 1 1 1c0 1.25.2 2.45.57 3.57a1 1 0 0 1-.25 1z"/></svg>
          0299990123
        </li>
        <li>
          <svg viewBox="0 0 24 24" aria-hidden="true"><rect x="2" y="5" width="20" height="14" rx="1.5" fill="var(--orange)"/><path d="M3 6l9 7 9-7" fill="none" stroke="#fff" stroke-width="1.6"/></svg>
          info@northgatehydraulics.com.au
        </li>
        <li>
          <svg viewBox="0 0 24 24" aria-hidden="true" fill="none" stroke="var(--orange)" stroke-width="1.6"><circle cx="12" cy="12" r="9.5"/><ellipse cx="12" cy="12" rx="4" ry="9.5"/><path d="M2.5 12h19M4 7h16M4 17h16"/></svg>
          www.northgatehydraulics.com.au
        </li>
      </ul>
      <p class="address">12 Wattle St, Riverton<br>South NSW 2999</p>
    </div>
  </section>
</body>
</html>
```